Thai Menu Design Project

We need a new menu design for a Thai restaurant in Fort Worth, Texas. We are a family-owned and really proud about our food and our service. We want the menu to feel healthy, modern, delicious, artistic Thai, and friendly. The colors we used in our restaurant are maroon, burgundy, black, white, gold and pale yellow.

Please look at our website www.brindlewokery.com
for the reference of the menus and the photos we use.

The menu can be in any number of pages (the fewer the better though) The size of the paper is US letter.
Updates

Update:

- We don't put the photos of the food in the menu pages anymore, instead, we like to put the photos of the herbs and their benefits (found in the file 'herb benefits') on the menu pages instead.

- the paper size is US letter.

- we don't have specific numbers of pages but the fewer the better

Thank you!

I added logos and background photo again in case the previous files did not work. Thanks!

Target Market(s)

Trendy socialized people from 20-30s,couples of all ages from 20s-60s,and families.

Industry/Entity Type

Restaurant

Requirements
Must have
• We want the menu to feel healthy, modern, delicious, artistic, Thai, and friendly.

We like to keep the colors maroon, burgundy, black, gold, pale yellow, and off white.

We like to put the photos of the herbs and their benefits (available in the file called 'herb benefits') randomly in the menu pages.

*Please use the photos available in the file called 'herb benefits' along with its details somewhere in the pages. You can change the photo of each herb to the ones you find more fitting from the internet.

Nice to have
• If we can add the wallpaper pattern in our menu it will be great. It can be used in anyway.

```html
<!DOCTYPE html>
<html lang="en">
<head>
<meta charset="utf-8">
<title>Brindle Wokery Menu</title>
<link rel="stylesheet" href="https://fonts.googleapis.com/css2?family=Arimo:ital,wght@0,400;0,700;1,400&family=Great+Vibes&display=swap">
<style>
  :root {
    --page-bg: #ffffff;
    --plum-deep: #3a0b29;
    --plum-dark: #4a1237;
    --plum-panel: #2e0820;
    --plum-cover: #6c2159;
    --gold: #c9a86a;
    --gold-soft: #b89a62;
    --item-yellow: #e9c34b;
    --soup-pink: #eaa2c0;
    --veg-green: #86c140;
    --spicy-red: #e0464b;
    --cream: #f1e6c8;
    --text-light: #f3ecf0;
    --body-font: "Arimo", Arial, sans-serif;
    --script-font: "Great Vibes", cursive;
  }
  * { box-sizing: border-box; margin: 0; padding: 0; }
  html, body { width: 1200px; height: 1000px; overflow: hidden; background: var(--page-bg); }
  body { position: relative; font-family: var(--body-font); }

  /* Cover page */
  .cover { position: absolute; left: 0; top: 104px; width: 598px; height: 780px; background: var(--plum-deep); overflow: hidden; }
  .cover-pattern { position: absolute; left: 0; top: 46px; width: 598px; height: 648px;
    background: radial-gradient(ellipse at 50% 50%, #8a3a72 0%, var(--plum-cover) 45%, #4e1440 100%); }
  .cover-pattern::after { content: ""; position: absolute; inset: 0;
    background: repeating-linear-gradient(90deg, rgba(201,168,106,0.18) 0 70px, rgba(201,168,106,0.05) 70px 150px); }
  .cover-band { position: absolute; left: 0; width: 598px; }
  .band-line-top { top: 354px; height: 3px; background: var(--gold-soft); }
  .band-main { top: 362px; height: 46px; background: rgba(241,230,200,0.55); }
  .band-line-bottom { top: 412px; height: 3px; background: var(--gold-soft); }
  .brand { position: absolute; left: 0; top: 356px; width: 598px; text-align: center; }
  .brand-name { font-size: 34px; font-weight: 700; color: var(--plum-dark); letter-spacing: 1px; line-height: 40px; }
  .brand-tag { font-size: 12px; color: var(--plum-dark); line-height: 14px; }
  .cover-footer { position: absolute; left: 0; top: 694px; width: 598px; height: 86px; background: var(--plum-deep); text-align: center; }
  .address { margin-top: 14px; font-size: 12.5px; color: var(--text-light); letter-spacing: 0.3px; }
  .phone { font-size: 32px; color: var(--gold); line-height: 40px; }
  .phone small { font-size: 22px; }

  /* Inside page */
  .inside { position: absolute; left: 604px; top: 104px; width: 596px; height: 780px; background: var(--plum-dark); overflow: hidden; color: var(--text-light); }
  .panel { position: absolute; background: var(--plum-panel); border-radius: 10px; }
  .panel-appetizers { left: 12px; top: 14px; width: 212px; height: 228px; }
  .panel-salads { left: 6px; top: 236px; width: 222px; height: 540px; background: #3a0d2b; }
  .panel-soups { left: 232px; top: 362px; width: 360px; height: 414px; background: #3c0d2d; }

  .column { position: absolute; font-size: 9.2px; line-height: 1.15; }
  .section-title { font-family: var(--script-font); font-size: 28px; color: var(--cream); line-height: 30px; margin-bottom: 4px; }
  .item { margin-bottom: 9px; }
  .item-head { display: flex; justify-content: space-between; }
  .item-name { font-style: italic; color: var(--item-yellow); }
  .salads .item-name, .soups .item-name { font-style: normal; font-variant: small-caps; font-weight: 700; }
  .soups .item-name { color: var(--soup-pink); }
  .new { font-style: italic; color: var(--item-yellow); font-weight: 400; font-variant: normal; }
  .veg { color: var(--veg-green); font-style: normal; }
  .spicy { color: var(--spicy-red); }
  .opt { font-style: italic; }
  .price-row { display: flex; justify-content: space-between; }

  .col-appetizers { left: 18px; top: 20px; width: 198px; }
  .col-salads { left: 18px; top: 244px; width: 202px; }
  .col-mid { left: 234px; top: 22px; width: 172px; }
  .col-right { left: 412px; top: 22px; width: 172px; }
  .col-soups-left { left: 242px; top: 366px; width: 143px; }
  .col-soups-right { left: 456px; top: 494px; width: 132px; }
  .col-soups-right .item { margin-bottom: 8px; }
  .veg-note { position: absolute; left: 470px; top: 404px; width: 116px; font-size: 8.6px; font-style: italic; text-align: right; line-height: 1.15; }
  .footnote { position: absolute; left: 242px; top: 730px; width: 205px; font-size: 8.2px; font-style: italic; color: var(--item-yellow); line-height: 1.2; }

  .herb { position: absolute; border-radius: 40%; }
  .herb-ginger { left: 78px; top: 168px; width: 150px; height: 70px; background: linear-gradient(120deg, #e8d7a8 0%, #c9b07a 55%, #3f7a2a 100%); }
  .herb-lemongrass { left: 400px; top: 408px; width: 36px; height: 130px; border-radius: 16px; background: linear-gradient(180deg, #f2f0d8 0%, #cfe0a0 50%, #7aa83f 100%); transform: rotate(12deg); }
  .herb-basil { left: 306px; top: 644px; width: 84px; height: 80px; background: radial-gradient(circle, #7fc24a 0%, #3f8a2a 100%); }
</style>
</head>
<body>

<section class="cover">
  <div class="cover-pattern" role="img" aria-label="Gold damask floral wallpaper pattern on purple"></div>
  <div class="cover-band band-line-top"></div>
  <div class="cover-band band-main"></div>
  <div class="cover-band band-line-bottom"></div>
  <div class="brand">
    <div class="brand-name">Brindle Wokery</div>
    <div class="brand-tag">Healthy and Original Cooking</div>
  </div>
  <div class="cover-footer">
    <p class="address">2280 Harlow Avenue Suite 114 Fort Worth, Texas 76109</p>
    <p class="phone"><small>817-</small>555-0148</p>
  </div>
</section>

<section class="inside">
  <div class="panel panel-appetizers"></div>
  <div class="panel panel-salads"></div>
  <div class="panel panel-soups"></div>

  <div class="herb herb-ginger" role="img" aria-label="Photo of ginger root with a green leaf"></div>
  <div class="herb herb-lemongrass" role="img" aria-label="Photo of lemongrass stalks"></div>
  <div class="herb herb-basil" role="img" aria-label="Photo of Thai basil leaves"></div>

  <div class="column col-appetizers appetizers">
    <h2 class="section-title">Appetizers</h2>
    <div class="item"><div class="item-head"><span class="item-name">Chicken Satay (6)</span><span>9</span></div>Marinated chicken on skewers served with our famous peanut sauce &amp; cucumber salad</div>
    <div class="item"><div class="item-head"><span class="item-name">Coconut Shrimp (6) <span class="new">New!</span></span><span>8</span></div>Served with sweet spicy dipping sauce</div>
    <div class="item"><div class="item-head"><span class="item-name">Brindle Sampler</span><span>14</span></div>2 Chicken Satay, 2 Golden Shrimp, 2 Pot Stickers, 2 Crab Rangoon, &amp; 2 Crispy Spring Roll</div>
  </div>

  <div class="column col-salads salads">
    <h2 class="section-title">Salads &amp; Yum</h2>
    <div class="item"><div class="item-head"><span class="item-name">Larb <span class="spicy">*</span></span><span>10</span></div>North-Eastern spicy salad seasoned with herbs, shallots, scallions, roasted ground rice in spicy lime juice.<br>Choice of chicken, pork, or soft tofu.</div>
    <div class="item"><div class="item-head"><span class="item-name">Duck Salad <span class="new">New!</span></span><span>12</span></div>Marinated duck with tomatoes, onions, cilantro tossed with lime juice &amp; Thai chili</div>
    <div class="item"><div class="item-head"><span class="item-name">Yum Woon Sen <span class="spicy">*</span></span><span>10</span></div>Spicy glass noodles with shrimp, ground pork, onions, cilantro, tomatoes in lime juice &amp; chili</div>
    <div class="item"><div class="item-head"><span class="item-name">Som Tum (V) <span class="spicy">*</span></span><span>9</span></div>Papaya salad with Thai long green beans, tomatoes, &amp; peanuts in spicy homemade dressing</div>
    <div class="item"><div class="item-head"><span class="item-name">Yum Neu <span class="spicy">*</span></span><span>10</span></div>Marinated grilled beef with tomatoes, onions, cilantro tossed with lime juice &amp; Thai chili</div>
    <div class="item"><div class="item-head"><span class="item-name">Pla Goong <span class="spicy">*</span></span><span>11</span></div>Shrimp with cucumbers, tomatoes, onions, &amp; cilantro tossed with lime juice &amp; Thai chili</div>
    <div class="item"><div class="item-head"><span class="item-name">Spicy Seafood Salad <span class="spicy">*</span></span><span>12</span></div>Mixed seafood with sliced cucumber, tomatoes, onions, cilantro tossed with lime juice &amp; Thai chili</div>
    <div class="item"><div class="item-head"><span class="item-name">House Salad</span><span>7</span></div>Lettuce, onions, tomatoes &amp; sliced hard-boiled eggs with choice of Thai lime dressing or Thai peanut dressing
      <div class="price-row opt"><span>With Grilled Chicken</span><span>8.50</span></div>
      <div class="price-row opt"><span>With Grilled Shrimp</span><span>9.50</span></div></div>
    <div class="item"><div class="item-head"><span class="item-name">Nam Sod</span><span>10</span></div>Ground pork with lime juice, ginger, peanuts, onions &amp; cilantro</div>
  </div>

  <div class="column col-mid appetizers">
    <div class="item"><div class="item-head"><span class="item-name">Three Musketeers <span class="veg">(V)</span> <span class="new">New!</span></span><span>9</span></div>2 Awesome Taro, 2 Sweet Corn Cakes, &amp; 2 Crispy Tofu. All Vegetarians!</div>
    <div class="item"><div class="item-head"><span class="item-name">Fried Calamari</span><span>8</span></div>Battered calamari served with plum sauce</div>
    <div class="item"><div class="item-head"><span class="item-name">Crab Rangoon (6)</span><span>7.5</span></div>Crab with cream cheese in crispy wonton skin</div>
    <div class="item"><div class="item-head"><span class="item-name">Fish Cake (6) <span class="new">New!</span></span><span>8</span></div>Thai-style spicy fishcake served with cucumber vinaigrette</div>
    <div class="item"><div class="item-head"><span class="item-name">Thai Beef Jerky</span><span>9</span></div>Sliced fried beef marinated with Thai seasoning, served with flavorful dipping sauce</div>
    <div class="item"><div class="item-head"><span class="item-name">Sweet Corn Cake (5) <span class="veg">(V)</span></span><span>7.5</span></div>Seasoned sweet corn battered &amp; deep-fried served with sweet sauce</div>
    <div class="item"><div class="item-head"><span class="item-name">Chicken or Tofu Lettuce Wrap <span class="veg">(V)</span></span><span>9</span></div>Minced chicken or tofu, water chestnuts, mushrooms, scallions, crispy noodles &amp; cool lettuce cups with spicy lime sauce</div>
  </div>

  <div class="column col-right appetizers">
    <div class="item"><div class="item-head"><span class="item-name">Crispy Soft Shell Crabs (2)</span><span>8</span></div>Soft shell crabs fried to a light crisp served with sweet &amp; spicy sauce</div>
    <div class="item"><div class="item-head"><span class="item-name">Pot Stickers (8)</span><span>7.5</span></div>Pork &amp; cabbage dumplings served steamed or fried</div>
    <div class="item"><div class="item-head"><span class="item-name">Mixed Vegetable Tempura <span class="veg">(V)</span></span><span>9</span></div>Breaded green beans, eggplant, carrot, &amp; broccoli served with Thai ginger sauce</div>
    <div class="item"><div class="item-head"><span class="item-name">Cucumber Salad <span class="veg">(V)</span></span><span>5</span></div>Sliced cucumber in sweet vinaigrette</div>
    <div class="item"><div class="item-head"><span class="item-name">Edamame <span class="veg">(V)</span></span><span>5</span></div>Steamed salted soybeans</div>
    <div class="item"><div class="item-head"><span class="item-name">Crispy Spring Rolls (5)</span><span>7.50</span></div>Pork, carrot, cabbage, &amp; noodles in Thai spring roll wrapper<br><span class="item-name">Vegetarian Spring Rolls (5)</span> <span class="veg">(V)</span></div>
    <div class="item"><div class="item-head"><span class="item-name">Egg Roll (1)</span><span>1.65</span></div>Crispy eggroll stuffed with seasoned pork &amp; cabbage<br><span class="item-name">Vegetarian Egg Roll (V)</span></div>
    <div class="item"><div class="item-head"><span class="item-name">Summer Rolls (2) <span class="veg">(V)</span></span><span>3</span></div>Romaine lettuce, vermicelli, cilantro, carrot, &amp; red cabbage in rice wrapper served with peanut sauce<br><span class="opt">For Tofu or Shrimp add 1</span></div>
  </div>

  <div class="veg-note">* (V) for Vegetarian.<br>No substitute please.<br>Up to 5 credit card per check, thank you.</div>

  <div class="column col-soups-left soups">
    <h2 class="section-title">Soups</h2>
    <div class="item"><span class="item-name">Classic Tom Yum <span class="spicy">*</span></span><br>Spicy lemongrass soup with mushroom, cilantro, lime juice &amp; chili<br><span class="opt">With Shrimp or Mixed Vegetables</span><br>Bowl 7 &nbsp; Hot Pot 13.5<br><span class="opt">With mixed Seafood</span><br>Bowl 8 &nbsp; Hot Pot 15.5</div>
    <div class="item"><span class="item-name">Tom Yum Brindle <span class="spicy">*</span></span><br>Classic Tom Yum with coconut milk for a smooth taste.<br><span class="opt">With Shrimp or Mixed Vegetables</span><br>Bowl 7 &nbsp; Hot Pot 13.5<br><span class="opt">With mixed Seafood</span><br>Bowl 8 &nbsp; Hot Pot 15.5</div>
    <div class="item"><span class="item-name">Seafood Poh Taek <span class="spicy">*</span> <span class="new">New!</span></span><br>The full flavor of Thai super herbs, hot &amp; tangy yet light &amp; refreshing. Healthy &amp; delicious.<br>Hot Pot 15.5</div>
  </div>

  <div class="column col-soups-right soups">
    <div class="item"><span class="item-name">Tom Kha</span><br>Galangal coconut soup with mushroom, cilantro, chili, &amp; lime juice.<br><span class="opt">With Chicken, Mixed Vegetables, or Soft Tofu</span><br>Bowl 8 &nbsp; Hot Pot 13.5</div>
    <div class="item"><span class="item-name">Tom Sab E-Sarn <span class="spicy">*</span></span><br>North-Eastern spicy &amp; sour soup flavored with herbs. Choice of Pork, Chicken, or Mixed Vegetables.<br>Bowl 6 &nbsp; Hot Pot 11.5</div>
    <div class="item"><span class="item-name">Vegetable Tofu Soup <span class="veg">(V)</span></span><br>Thai style mild broth with mixed vegetable &amp; soft tofu. Soup for the soul<br>Bowl 5 &nbsp; Hot Pot 9.5</div>
    <div class="item"><span class="item-name">Wanton Soup <span class="new">New!</span></span><br>Bowl 5 &nbsp; Hot Pot 9.5</div>
  </div>

  <p class="footnote"><span class="spicy">*</span> For spicy dishes, please choose spicy level from 1 to 5.<br>(V) for Vegetarian. Up to 5 credit cards per check please.</p>
</section>

</body>
</html>
```